Business Card Design needed - Something Awesome!

Need a business card designed. Company is "Harbor Vane Consulting" we do consulting and also have sales automation technology.
I'm going to use thick stock or metal, something really nice... I was thinking about a QR Code on the back that would just upload my contact info to the persons contact, etc -

This is a Strategy Company with a tech feel. I'm open to ideas but really want this to be nice!

I need a template that should include:

Name | Position or Title
D: 987.654.3210
www.harborvaneconsulting.example

I'm going to attach my contact so you can use that one, I need to get this printed.

Target Market(s)

Small to mid size customers, Entrepreneurs etc.

Industry/Entity Type

Consulting, Tech, Private Equity.

Contact Information for Business Card

Name, Phone, Maybe email, URL

Font styles to use
Sans Serif

Colors

Designer to choose only greyscale colors for use in the design.

Requirements
Must have
• Fresh, Clean, stand out from the crowd - will be on thick stock or metal.
Nice to have
• Clean, simple yet impactful.
Should not have
• Not cartoonish

```html
<!DOCTYPE html>
<html lang="en">
<head>
<meta charset="utf-8">
<title>Harbor Vane Consulting — Business Card</title>
<link rel="stylesheet" href="https://fonts.googleapis.com/css2?family=Montserrat:wght@500;600&family=Carlito&display=swap">
<style>
  :root {
    --backdrop: #e6e6e6;
    --card-stock: #f4f4f3;
    --ink: #1f2a38;
    --ink-soft: #2b3441;
  }
  * { margin: 0; padding: 0; box-sizing: border-box; }
  html, body {
    width: 1200px;
    height: 900px;
    overflow: hidden;
    background: var(--backdrop);
  }
  .card {
    position: absolute;
    left: 80px;
    top: 153px;
    width: 1040px;
    height: 594px;
    background: var(--card-stock);
    color: var(--ink);
  }
  .holder-name {
    position: absolute;
    left: 28px;
    top: 66px;
    font-family: "Montserrat", sans-serif;
    font-weight: 600;
    font-size: 34px;
    letter-spacing: 0.2px;
  }
  .holder-title {
    position: absolute;
    left: 32px;
    top: 112px;
    font-family: "Montserrat", sans-serif;
    font-weight: 500;
    font-size: 21px;
    color: var(--ink-soft);
  }
  .address, .contact-list {
    position: absolute;
    left: 28px;
    font-family: "Carlito", sans-serif;
    font-size: 23px;
    line-height: 35px;
    color: var(--ink-soft);
    list-style: none;
  }
  .address { top: 296px; }
  .contact-list { top: 418px; }
  .wordmark {
    position: absolute;
    right: 66px;
    top: 258px;
    display: flex;
    align-items: center;
    gap: 14px;
  }
  .wordmark-square {
    width: 26px;
    height: 26px;
    background: var(--ink);
  }
  .wordmark-name {
    font-family: "Montserrat", sans-serif;
    font-weight: 600;
    font-size: 44px;
    letter-spacing: 1px;
    color: var(--ink);
  }
</style>
</head>
<body>
  <section class="card">
    <h1 class="holder-name">Dorian K. Ashby</h1>
    <p class="holder-title">Founder / CEO</p>

    <address class="address">
      42/118 Quay Road.<br>
      Unaite Kingdom
    </address>

    <ul class="contact-list">
      <li>Mob : 987.654.3210</li>
      <li>Email : emailaddresshere</li>
      <li>Web : www.harborvaneconsulting.example</li>
    </ul>

    <div class="wordmark">
      <span class="wordmark-square"></span>
      <span class="wordmark-name">HARBOR VANE</span>
    </div>
  </section>
</body>
</html>
```